Pest Control Company needs business card!

Hi there, we need a business card designed for our new Pest Control Company. Ideally this card will be simple, yet feel elegant and high end. We want to use the colours Orange, Black and White. Please see our attached logo for the exact colours.

Business card details:

Phone - 0461 275 804
Name - Gavin Holloway
Email - Info@steadfastverminguard.com.au

We would also like to include the following list with dot points:

SERVICES / INSPECTIONS

Termites, Wood Borers, Ants, Cockroaches, Spiders, Fleas, Mice, Rats, Bed Bugs, & More!

```html
<!DOCTYPE html>
<html lang="en">
<head>
<meta charset="utf-8">
<title>Steadfast Vermin Guard – Business Card</title>
<link href="https://fonts.googleapis.com/css2?family=Montserrat:wght@400;500;700;800&display=swap" rel="stylesheet">
<style>
  :root {
    --backdrop: #b9b9b9;
    --card: #232323;
    --card-light: #2e2e2e;
    --orange: #f28a2a;
    --white: #f2f2f2;
  }
  * { margin: 0; padding: 0; box-sizing: border-box; }
  html, body { width: 1200px; height: 675px; overflow: hidden; }
  body {
    background: var(--backdrop);
    font-family: "Montserrat", sans-serif;
    display: flex;
    align-items: center;
    justify-content: center;
    gap: 48px;
  }
  .card {
    position: relative;
    width: 520px;
    height: 298px;
    border-radius: 18px;
    background: linear-gradient(135deg, var(--card) 0%, var(--card-light) 45%, var(--card) 100%);
    box-shadow: 0 10px 24px rgba(0,0,0,0.25);
    overflow: hidden;
    color: var(--white);
  }
  .brand {
    display: flex;
    align-items: center;
    gap: 12px;
  }
  .brand-dot {
    width: 30px;
    height: 30px;
    border-radius: 50%;
    background: var(--orange);
    flex: none;
  }
  .brand-name {
    font-weight: 800;
    color: var(--orange);
    text-transform: uppercase;
    line-height: 1.02;
    letter-spacing: 0.5px;
  }

  /* Front */
  .card-front .brand { position: absolute; left: 38px; top: 42px; }
  .card-front .brand-name { font-size: 24px; }
  .holder-name {
    position: absolute;
    right: 40px;
    top: 188px;
    font-size: 19px;
    font-weight: 500;
    color: var(--orange);
    text-transform: uppercase;
    letter-spacing: 0.5px;
  }
  .rule {
    position: absolute;
    height: 1px;
    background: var(--orange);
  }
  .card-front .rule-top { left: 38px; right: 40px; top: 220px; }
  .card-front .rule-bottom { left: 270px; right: 40px; top: 268px; }
  .contact {
    position: absolute;
    display: flex;
    align-items: center;
    gap: 9px;
    font-size: 13.5px;
    font-weight: 500;
  }
  .contact svg { width: 15px; height: 15px; fill: var(--orange); flex: none; }
  .contact-email { left: 38px; top: 232px; }
  .contact-phone { right: 40px; top: 236px; }

  /* Back */
  .card-back .brand {
    position: absolute;
    left: 0; right: 0; top: 58px;
    justify-content: center;
  }
  .card-back .brand-dot { width: 40px; height: 40px; }
  .card-back .brand-name { font-size: 30px; }
  .card-back .rule { left: 50px; right: 50px; top: 178px; }
  .services-title {
    position: absolute;
    left: 0; right: 0; top: 192px;
    text-align: center;
    font-size: 12px;
    font-weight: 500;
    letter-spacing: 0.6px;
    text-transform: uppercase;
  }
  .services-list {
    position: absolute;
    left: 30px; right: 30px; top: 222px;
    text-align: center;
    font-size: 11.5px;
    font-weight: 400;
    line-height: 1.6;
  }
</style>
</head>
<body>
  <section class="card card-front">
    <div class="brand">
      <span class="brand-dot"></span>
      <span class="brand-name">Steadfast<br>Vermin<br>Guard</span>
    </div>
    <p class="holder-name">Gavin Holloway</p>
    <div class="rule rule-top"></div>
    <p class="contact contact-email">
      <svg viewBox="0 0 24 24" aria-hidden="true"><path d="M2 5h20v14H2z M3.5 6.5v.4L12 13l8.5-6.1v-.4z" fill-rule="evenodd"/></svg>
      Info@steadfastverminguard.com.au
    </p>
    <p class="contact contact-phone">
      <svg viewBox="0 0 24 24" aria-hidden="true"><path d="M6.6 10.8a15 15 0 0 0 6.6 6.6l2.2-2.2a1 1 0 0 1 1-.25 11.4 11.4 0 0 0 3.6.57 1 1 0 0 1 1 1V20a1 1 0 0 1-1 1A17 17 0 0 1 3 4a1 1 0 0 1 1-1h3.5a1 1 0 0 1 1 1c0 1.25.2 2.45.57 3.57a1 1 0 0 1-.25 1z"/></svg>
      0461 275 804
    </p>
    <div class="rule rule-bottom"></div>
  </section>

  <section class="card card-back">
    <div class="brand">
      <span class="brand-dot"></span>
      <span class="brand-name">Steadfast<br>Vermin<br>Guard</span>
    </div>
    <div class="rule"></div>
    <p class="services-title">Services / Inspections</p>
    <p class="services-list">Termites, Wood Borers, Ants, Cockroaches, Spiders, Fleas, Mice, Rats, Bed Bugs, &amp; More!</p>
  </section>
</body>
</html>
```